Marketing Flyer

We are looking for a flyer that will clearly and simply explain that we are an internet, tv, and telephone provider for the business community. we compete with major providers. we offer a triple play package as well tv internet and phone

Target Market(s)

small to medium sixed business

Industry/Entity Type

Telecom

Font styles to use
Serif

Colors

Designer to choose colors to be used in the design.

Requirements
Must have
• logo, hip, current industry buzz words fun life
Nice to have
• color,
Should not have
• must not be dull and over simple

```html
<!DOCTYPE html>
<html lang="en">
<head>
<meta charset="utf-8">
<title>Brightline Tech – Business Internet, TV &amp; Phone Flyer</title>
<link rel="stylesheet" href="https://fonts.googleapis.com/css2?family=Arimo:ital,wght@0,400;0,700;1,700&family=Oswald:wght@500;700&display=swap">
<style>
  :root {
    --orange: #e8501c;
    --orange-dark: #c8400f;
    --navy: #222b3d;
    --ink: #1f1f24;
    --text: #2a2a2a;
    --paper: #ffffff;
    --rule: #9a9a9a;
    --photo-light: #eef0f1;
    --photo-mid: #c9ccce;
  }
  * { margin: 0; padding: 0; box-sizing: border-box; }
  html, body { width: 850px; height: 1200px; overflow: hidden; background: var(--paper); }
  .flyer { position: relative; width: 850px; height: 1200px; background: var(--paper); font-family: "Arimo", Arial, sans-serif; color: var(--text); overflow: hidden; }
  .shapes { position: absolute; inset: 0; }
  .site-url { position: absolute; left: 46px; top: 48px; font-size: 29px; color: var(--ink); }
  .brand { position: absolute; left: 440px; top: 92px; width: 400px; text-align: center; }
  .brand-row { display: flex; align-items: center; justify-content: center; gap: 12px; }
  .brand-mark { width: 30px; height: 30px; background: var(--navy); }
  .brand-name { font-size: 30px; font-weight: 400; letter-spacing: 1.5px; color: var(--orange); text-transform: uppercase; }
  .brand-tagline { margin-top: 4px; font-style: italic; font-weight: 700; font-size: 14px; color: var(--navy); letter-spacing: .3px; }
  .photo { position: absolute; left: 372px; top: 163px; width: 478px; height: 395px; background: linear-gradient(110deg, var(--photo-mid) 0%, var(--photo-light) 55%, #dfe1e2 100%); }
  .staff-panel { position: absolute; left: 30px; top: 172px; width: 292px; color: #fff; }
  .staff-title { font-family: "Oswald", Impact, sans-serif; font-weight: 700; font-size: 34px; line-height: 44px; letter-spacing: .3px; margin-bottom: 14px; }
  .staff-panel p { font-size: 13.2px; line-height: 15.6px; margin-bottom: 15px; }
  .headline { position: absolute; left: 46px; top: 578px; font-family: "Oswald", Impact, sans-serif; font-weight: 700; font-size: 29px; line-height: 37px; color: var(--ink); }
  .section-tab { position: absolute; left: 0; height: 44px; width: 315px; background: var(--orange); border-radius: 0 12px 12px 0; box-shadow: 0 6px 8px -4px rgba(0,0,0,.45); color: #fff; font-family: "Oswald", Impact, sans-serif; font-weight: 700; font-size: 30px; line-height: 42px; padding-left: 54px; }
  .tab-who { top: 667px; }
  .tab-what { top: 880px; width: 325px; }
  .about { position: absolute; left: 53px; top: 724px; width: 767px; font-size: 13.9px; line-height: 17.6px; text-align: justify; color: var(--ink); }
  .services { position: absolute; top: 940px; left: 0; width: 850px; }
  .service-col { position: absolute; top: 0; list-style: none; }
  .service-col li { position: relative; font-size: 13.6px; line-height: 23.5px; padding-left: 19px; color: var(--ink); white-space: nowrap; }
  .service-col li svg { position: absolute; left: 0; top: 7px; }
  .col-1 { left: 43px; } .col-2 { left: 305px; } .col-3 { left: 590px; }
  .col-divider { position: absolute; top: 944px; width: 1px; height: 150px; background: var(--rule); }
  .contact-address { position: absolute; left: 43px; top: 1114px; display: flex; gap: 8px; font-size: 16px; line-height: 18.5px; color: var(--ink); font-style: normal; }
  .contact-direct { position: absolute; left: 405px; top: 1116px; font-size: 21px; color: var(--ink); }
  .contact-direct div { display: flex; align-items: center; gap: 8px; height: 29px; }
  .phone-number { font-weight: 700; }
  .footer-divider { position: absolute; top: 1118px; width: 1px; height: 64px; background: var(--rule); }
  .follow { position: absolute; left: 680px; top: 1115px; font-size: 20px; color: var(--ink); }
  .social { display: flex; gap: 5px; margin-top: 6px; margin-left: 11px; }
  .social span { width: 20px; height: 20px; border: 1.6px solid var(--ink); border-radius: 50%; }
</style>
</head>
<body>
<main class="flyer">
  <div class="photo" role="img" aria-label="Photo of a man in glasses and a white shirt working at a laptop in a bright office"></div>

  <svg class="shapes" width="850" height="1200" viewBox="0 0 850 1200" aria-hidden="true">
    <polygon points="0,0 52,0 0,72" fill="var(--orange)"/>
    <polygon points="70,112 372,112 372,125 70,125" fill="var(--orange)"/>
    <polygon points="372,112 378,570 395,570 388,112" fill="var(--orange)"/>
    <polygon points="0,128 372,128 372,566 0,566" fill="var(--navy)"/>
    <polygon points="0,566 372,566 378,585 0,585" fill="#9b9fa6"/>
    <polygon points="378,548 850,540 850,574 540,574" fill="var(--orange)"/>
    <polygon points="560,574 850,574 850,580 600,580" fill="var(--orange-dark)"/>
    <polygon points="790,1189 850,1148 850,1189" fill="var(--navy)"/>
    <rect x="0" y="1189" width="850" height="11" fill="var(--navy)"/>
  </svg>

  <div class="site-url">www.brightline.tech</div>

  <div class="brand">
    <div class="brand-row"><span class="brand-mark"></span><span class="brand-name">Brightline Tech</span></div>
    <div class="brand-tagline">"Business Internet, TV &amp; Phone Provider"</div>
  </div>

  <section class="staff-panel">
    <h2 class="staff-title">Industry Best Staff !</h2>
    <p>Our team of engineers, installers, support technicians and account managers brings years of telecom experience to local businesses. We design, install and support your internet, TV and phone service so you get big-carrier power with a local, personal touch, when and where you need it.</p>
    <p>Connectivity moves fast, and so do we. We compete head to head with the major providers on speed, price and reliability, and we beat them on service. From fiber internet and crystal-clear cloud phones to HD business TV, we bring the latest tech to your door with one easy bill and one number to call.</p>
  </section>

  <h1 class="headline">Internet, TV &amp; Phone in one Triple Play,<br>built to drive your business results !</h1>

  <div class="section-tab tab-who">who we are?</div>
  <p class="about">Brightline Tech is an internet, TV and telephone provider built for the business community. Small and medium sized businesses deserve the same speed, uptime and features the major providers offer, without long hold times, hidden fees or confusing contracts. Our Triple Play package bundles high-speed business internet, HD business TV and cloud phone service into one plan, one install and one monthly bill. Prefer just one or two services? Choose internet, TV or phone on its own, or mix and match what you need. Every plan includes local support, fast installation and network monitoring, so you can focus on running your business while we keep you connected. Stream, call, post and grow with Brightline: fiber-fast internet, crystal-clear VoIP calling and TV for lobbies, waiting rooms and break areas.</p>

  <div class="section-tab tab-what">what we provide?</div>

  <svg width="0" height="0" style="position:absolute" aria-hidden="true">
    <symbol id="tick" viewBox="0 0 12 12"><path d="M1 6.5 L4.5 10 L11 1.5" fill="none" stroke="var(--orange)" stroke-width="2" stroke-linecap="round" stroke-linejoin="round"/></symbol>
  </svg>

  <div class="services">
    <ul class="service-col col-1">
      <li><svg width="12" height="12"><use href="#tick"/></svg>Triple Play: Internet, TV &amp; Phone</li>
      <li><svg width="12" height="12"><use href="#tick"/></svg>High-Speed Business Internet</li>
      <li><svg width="12" height="12"><use href="#tick"/></svg>Fiber &amp; Dedicated Internet</li>
      <li><svg width="12" height="12"><use href="#tick"/></svg>Managed Wi-Fi Networks</li>
      <li><svg width="12" height="12"><use href="#tick"/></svg>Static IP Addresses</li>
      <li><svg width="12" height="12"><use href="#tick"/></svg>Backup Internet &amp; Failover</li>
      <li><svg width="12" height="12"><use href="#tick"/></svg>Onsite and Remote Support</li>
    </ul>
    <ul class="service-col col-2">
      <li><svg width="12" height="12"><use href="#tick"/></svg>HD Business TV Packages</li>
      <li><svg width="12" height="12"><use href="#tick"/></svg>TV for Lobbies &amp; Waiting Rooms</li>
      <li><svg width="12" height="12"><use href="#tick"/></svg>Sports, News &amp; Music Channels</li>
      <li><svg width="12" height="12"><use href="#tick"/></svg>Digital Signage</li>
      <li><svg width="12" height="12"><use href="#tick"/></svg>Streaming-Ready TV Service</li>
      <li><svg width="12" height="12"><use href="#tick"/></svg>One Install, One Monthly Bill</li>
      <li><svg width="12" height="12"><use href="#tick"/></svg>No Hidden Fees or Surprises</li>
    </ul>
    <ul class="service-col col-3">
      <li><svg width="12" height="12"><use href="#tick"/></svg>Voice over IP Phone System (VoIP)</li>
      <li><svg width="12" height="12"><use href="#tick"/></svg>Cloud Phones &amp; Mobile App</li>
      <li><svg width="12" height="12"><use href="#tick"/></svg>Unlimited Local &amp; Long Distance</li>
      <li><svg width="12" height="12"><use href="#tick"/></svg>Auto Attendant &amp; Voicemail</li>
      <li><svg width="12" height="12"><use href="#tick"/></svg>Keep Your Business Number</li>
      <li><svg width="12" height="12"><use href="#tick"/></svg>World Wide Calling Plans</li>
    </ul>
  </div>
  <div class="col-divider" style="left:289px"></div>
  <div class="col-divider" style="left:576px"></div>

  <address class="contact-address">
    <svg width="16" height="22" viewBox="0 0 16 22" aria-hidden="true"><path d="M8 1a6 6 0 0 0-6 6c0 4.5 6 11 6 11s6-6.5 6-11a6 6 0 0 0-6-6z" fill="none" stroke="#777" stroke-width="1.5"/><circle cx="8" cy="7" r="2.2" fill="none" stroke="#777" stroke-width="1.5"/><path d="M1 20.5h14" stroke="#777" stroke-width="1.5"/></svg>
    <span>Brightline Tech Solutions,<br>418 Harbor Road, Millbrook, NJ 07990<br>Corporate Headquarters</span>
  </address>

  <div class="footer-divider" style="left:387px"></div>

  <div class="contact-direct">
    <div><svg width="16" height="16" viewBox="0 0 16 16" aria-hidden="true"><path d="M3.5 1.5l2.5 3-1.5 1.8a9 9 0 0 0 5.2 5.2l1.8-1.5 3 2.5-1.6 2A12 12 0 0 1 1.5 3.1z" fill="none" stroke="var(--ink)" stroke-width="1.5" stroke-linejoin="round"/></svg><span class="phone-number">555.014.2290</span></div>
    <div><svg width="18" height="18" viewBox="0 0 18 18" aria-hidden="true"><circle cx="9" cy="9" r="8.5" fill="var(--ink)"/><rect x="4.5" y="5.8" width="9" height="6.4" fill="none" stroke="#fff" stroke-width="1.2"/><path d="M4.5 6l4.5 3.5L13.5 6" fill="none" stroke="#fff" stroke-width="1.2"/></svg><span>info@brightline.tech</span></div>
  </div>

  <div class="footer-divider" style="left:647px"></div>

  <div class="follow">
    Follow Us On
    <div class="social" aria-hidden="true"><span></span><span></span><span></span><span></span></div>
  </div>
</main>
</body>
</html>
```